Web design for a relaunch of a technology and knowledge transfer company

Design for the relaunch of an existing website The company specializes in technology and knowledge transfer between companies (and universities). The innovation company (company name) combines many years of experience in technology transfer, innovation management, project management and grant applications. Link: http://www.vorlaufwerkstatt.example The colors of the logo are not very advantageous and can be adjusted a bit. There are currently no picture worlds, these are to be selected by the designer. Abstract motifs are certainly an advantage here (10 motifs). Animated programming could be done (network etc. http://pelvart.qmstudio.example/). In this case a suggestion is made, which we convert programming technically. The structure and contents of the existing pages will be adopted and supplemented. The programming will be done with TYPO3 in responsive form (bootstrap). Required are start page, content page and contact page. -------------------------------------------------- ------------------------------ Web design for a relaunch of a company in technology and knowledge transfer Design for the relaunch of an existing website. The company specializes in technology and knowledge transfer between companies (and universities). The innovation company combines many years of experience in the fields of technology transfer, innovation management, project management and grant application. Link: http://www.vorlaufwerkstatt.example The color of the logo is not exactly advantageous and can be adjusted. There are currently no image worlds, these are to be selected by the designer. Abstract motifs are certainly an advantage here (10 motifs). It could also be made animated programming (network, etc. http://pelvart.qmstudio.example/). In this case, a proposal has to be made, which we implement in terms of programming technology. The structure and contents of the existing pages are taken over and supplemented. Programming is done with TYPO3 in responsive form (bootstrap). Required are homepage, content page and contact page.

```html
<!DOCTYPE html>
<html lang="en">
<head>
<meta charset="utf-8">
<title>Vorlaufwerkstatt – Technology and Knowledge Transfer</title>
<link href="https://fonts.googleapis.com/css2?family=Poppins:wght@500;600;700;800&family=Open+Sans:wght@400;600&display=swap" rel="stylesheet">
<style>
:root{
  --navy:#1d1f9c;
  --red:#e1111d;
  --ink:#1e1e22;
  --text:#3a3a40;
  --soft:#f4f2f3;
  --line:#d9d7d8;
  --footer:#222224;
  --footer-text:#d6d6d8;
}
*{box-sizing:border-box;margin:0;padding:0}
html,body{width:1200px;height:3152px;overflow:hidden}
body{position:relative;font-family:"Open Sans",Arial,sans-serif;color:var(--text);background:#fff}
.abs{position:absolute}
h1,h2,h3,h4{font-family:"Poppins",Arial,sans-serif;color:var(--ink)}

/* header */
.site-header{position:absolute;left:0;top:0;width:1200px;height:130px;background:#fff}
.brand{position:absolute;display:flex;align-items:center;gap:12px;font-family:"Open Sans",sans-serif;font-weight:600;font-size:17px;letter-spacing:.4px}
.brand .mark{width:22px;height:22px;border:3px solid currentColor}
.site-header .brand{left:131px;top:62px;color:var(--navy)}
.call{position:absolute;left:618px;top:24px;display:flex;gap:10px;align-items:flex-start}
.call small{display:block;font-family:"Poppins",sans-serif;font-weight:700;font-size:12px;color:var(--ink)}
.call strong{display:block;font-family:"Poppins",sans-serif;font-weight:700;font-size:21px;color:var(--red);line-height:1.15;letter-spacing:-.3px;white-space:nowrap}
.search{position:absolute;left:892px;top:28px;width:175px;height:36px;border:1px solid #bbb;font-size:10px;color:#666;padding:11px 14px;letter-spacing:.5px}
.search svg{position:absolute;right:12px;top:12px}
.main-nav{position:absolute;right:133px;top:94px;display:flex;gap:26px;font-family:"Poppins",sans-serif;font-weight:600;font-size:13px;color:var(--ink)}
.main-nav .active{color:var(--red)}

/* hero */
.hero{position:absolute;left:0;top:130px;width:1200px;height:547px}
.hero-photo{position:absolute;inset:0;background:linear-gradient(110deg,#6f747c 0%,#b9bdc2 35%,#d8d8d6 55%,#9aa0a6 80%,#5f656c 100%)}
.hero-panel{position:absolute;left:667px;top:53px;width:533px;height:183px;background:rgba(255,255,255,.85);padding:22px 40px}
.hero-panel h1{color:var(--navy);font-weight:800;font-size:38px;line-height:1.05}
.hero-panel p{font-size:16px;color:#333;margin-top:12px;line-height:1.4}
.dots{position:absolute;left:544px;top:477px;display:flex;gap:12px;align-items:center}
.dots span{width:9px;height:9px;border-radius:50%;background:#fff}
.dots .on{width:13px;height:13px;background:transparent;border:2px solid #fff}

/* sections */
.section-title{position:absolute;left:0;width:1200px;text-align:center;font-weight:800;font-size:40px;letter-spacing:.5px}
.title-bar{position:absolute;left:580px;width:40px;height:4px;background:var(--navy)}

.services{position:absolute;left:0;top:677px;width:1200px;height:801px;background:var(--soft)}
.service{position:absolute;width:430px}
.service h3{font-weight:700;font-size:17px;line-height:1.25}
.service p{font-size:13px;line-height:1.45;margin-top:8px;color:#333}
.icon-box{position:absolute;width:86px;height:86px;border:3px solid var(--navy);border-radius:6px;background:#fff;display:flex;align-items:center;justify-content:center}
.divider-h{position:absolute;height:1px;background:var(--line)}
.divider-v{position:absolute;width:1px;background:var(--line)}
.btn{position:absolute;background:var(--red);color:#fff;font-family:"Poppins",sans-serif;font-weight:700;font-size:14px;text-align:center}

.welcome{position:absolute;left:0;top:1478px;width:1200px;height:632px;background:#fff}
.welcome-photo{position:absolute;left:131px;top:72px;width:402px;height:475px;background:radial-gradient(circle at 50% 40%,#8fb4ea 0%,#2b4d96 40%,#0d1838 100%)}
.welcome h2{position:absolute;left:580px;top:66px;font-weight:600;font-size:24px;line-height:1.2}
.welcome h2 b{display:block;font-weight:800;font-size:30px}
.welcome ul{position:absolute;left:583px;top:170px;width:520px;list-style:none}
.welcome li{position:relative;padding-left:32px;font-size:15px;line-height:1.4;margin-bottom:19px;color:#333}
.welcome li svg{position:absolute;left:0;top:4px}

.events{position:absolute;left:0;top:2110px;width:1200px;height:650px;background:var(--soft)}
.card{position:absolute;top:180px;width:240px;height:404px;background:#fff}
.card-photo{height:200px}
.card h3{font-weight:700;font-size:15.5px;line-height:1.3;margin:22px 22px 0;letter-spacing:-.2px;white-space:nowrap}
.card p{font-size:12.5px;line-height:1.45;margin:10px 22px 0;color:#333}
.card .btn{left:28px;top:346px;width:92px;height:32px;line-height:32px;font-size:11px}

.site-footer{position:absolute;left:0;top:2760px;width:1200px;height:392px;background:var(--footer);color:var(--footer-text)}
.site-footer .brand{left:135px;top:120px;color:#fff}
.site-footer h4{color:#fff;font-weight:700;font-size:12px;letter-spacing:.3px}
.f-col{position:absolute;top:70px;font-size:11px;line-height:1.5}
.f-row{display:flex;gap:14px;margin-top:20px}
.f-menu li{list-style:none;line-height:17.5px}
.social{display:flex;align-items:center;gap:14px;margin-top:15px}
.social span.c{width:26px;height:26px;border-radius:50%;background:#1f5bb0}
.footer-rule{position:absolute;left:133px;top:285px;width:934px;height:1px;background:#3a3a3c}
.copyright{position:absolute;left:0;top:333px;width:1200px;text-align:center;font-size:11px}
</style>
</head>
<body>

<header class="site-header">
  <div class="brand"><span class="mark"></span>VORLAUFWERKSTATT</div>
  <div class="call">
    <svg width="30" height="30" viewBox="0 0 24 24"><path fill="#1d1f9c" d="M6.6 10.8a15.1 15.1 0 0 0 6.6 6.6l2.2-2.2c.3-.3.7-.4 1-.2 1.1.4 2.3.6 3.6.6.6 0 1 .4 1 1V20c0 .6-.4 1-1 1A17 17 0 0 1 3 4c0-.6.4-1 1-1h3.5c.6 0 1 .4 1 1 0 1.3.2 2.5.6 3.6.1.3 0 .7-.2 1z"/></svg>
    <div><small>CALL US NOW</small><strong>+49 5100 24 61 380</strong></div>
  </div>
  <div class="search">SEARCH
    <svg width="11" height="11" viewBox="0 0 12 12"><circle cx="5" cy="5" r="3.8" fill="none" stroke="#444" stroke-width="1.5"/><path d="M8 8l3 3" stroke="#444" stroke-width="1.5"/></svg>
  </div>
  <nav class="main-nav">
    <span class="active">HOME</span><span>SERVICES</span><span>REFERENCES</span><span>EVENTS &amp; WORKSHOPS</span><span>REPORTS</span><span>CONTACT US</span>
  </nav>
</header>

<section class="hero">
  <div class="hero-photo" role="img" aria-label="Photo of a team meeting in a bright conference room"></div>
  <div class="hero-panel">
    <h1>THE LEAD<br>WORKSHOP</h1>
    <p>is a technology and knowledge transfer company that supports companies in implementing their innovative ideas.</p>
  </div>
  <div class="dots"><span></span><span></span><span class="on"></span><span></span><span></span></div>
</section>

<section class="services">
  <h2 class="section-title" style="top:56px">OUR SERVICES</h2>
  <div class="title-bar" style="top:121px"></div>

  <div class="divider-v" style="left:588px;top:185px;height:84px"></div>
  <div class="divider-v" style="left:588px;top:520px;height:84px"></div>
  <div class="divider-h" style="left:131px;top:323px;width:423px"></div>
  <div class="divider-h" style="left:622px;top:323px;width:445px"></div>
  <div class="divider-h" style="left:131px;top:496px;width:423px"></div>
  <div class="divider-h" style="left:622px;top:496px;width:445px"></div>

  <div class="icon-box" style="left:131px;top:204px"><svg width="44" height="44" viewBox="0 0 24 24"><path fill="#2a2a2e" d="M12 2a8 8 0 0 0-8 8l-2 4h2v4h4v4h8v-6a8 8 0 0 0-4-14z"/><circle cx="12" cy="10" r="3" fill="#fff"/></svg></div>
  <div class="service" style="left:243px;top:201px"><h3>Technology and<br>knowledge transfer</h3><p>We support companies in implementing<br>their innovative projects.</p></div>

  <div class="icon-box" style="left:981px;top:204px"><svg width="44" height="44" viewBox="0 0 24 24"><path fill="none" stroke="#2a2a2e" stroke-width="2" d="M3 12l9-8 9 8M6 10v10h12V10"/><rect x="10" y="14" width="4" height="6" fill="#2a2a2e"/></svg></div>
  <div class="service" style="left:650px;top:201px"><h3>Property Rights<br>and Co.</h3><p>As soon as an idea is transformed into a<br>product or process innovation...</p></div>

  <div class="icon-box" style="left:131px;top:370px"><svg width="44" height="44" viewBox="0 0 24 24"><circle cx="12" cy="10" r="7" fill="#2a2a2e"/><path d="M9 10l3 3 3-3" stroke="#fff" stroke-width="2" fill="none"/><rect x="9" y="18" width="6" height="2" fill="#2a2a2e"/><rect x="10" y="21" width="4" height="1.5" fill="#2a2a2e"/></svg></div>
  <div class="service" style="left:243px;top:367px"><h3>Innovation and project<br>management</h3><p>The management of innovation processes in<br>the sense of a systematic planning...</p></div>

  <div class="icon-box" style="left:981px;top:370px"><svg width="44" height="44" viewBox="0 0 24 24"><path fill="#2a2a2e" d="M12 3a7 7 0 0 0-7 7c0 2 1 3.5 2 4.5V20h7v-3h3a2 2 0 0 0 2-2v-2l2-1-2-3a7 7 0 0 0-7-6z"/></svg></div>
  <div class="service" style="left:650px;top:367px"><h3>From ideas to innovations</h3><p>Ideas do not hold, something must be done<br>with them." This quotation from English<br>mathematician and philosopher Edmund</p></div>

  <div class="icon-box" style="left:131px;top:535px"><svg width="46" height="46" viewBox="0 0 24 24"><circle cx="12" cy="5" r="2.5" fill="#2a2a2e"/><path d="M8 12a4 4 0 0 1 8 0z" fill="#2a2a2e"/><circle cx="5" cy="15" r="2.3" fill="#2a2a2e"/><circle cx="19" cy="15" r="2.3" fill="#2a2a2e"/><path d="M1 22a4 4 0 0 1 8 0zM15 22a4 4 0 0 1 8 0z" fill="#2a2a2e"/><path d="M12 12v3M8 17l4-2 4 2" stroke="#2a2a2e" fill="none"/></svg></div>
  <div class="service" style="left:243px;top:532px"><h3>Cooperation and network<br>management</h3><p>The development and implementation of<br>projects in cooperation with partners...</p></div>

  <div class="icon-box" style="left:981px;top:535px"><svg width="44" height="44" viewBox="0 0 24 24"><path fill="#2a2a2e" d="M3 9h4l10-5v16L7 15H3zM7 15l2 6h3l-2-6z"/><path d="M19 10v4" stroke="#2a2a2e" stroke-width="2"/></svg></div>
  <div class="service" style="left:650px;top:532px"><h3>All about money - promotion</h3><p>No company aligns its investments with<br>public funding. Nevertheless, it makes sense<br>to find out about the support options for<br>planned projects.</p></div>

  <div class="btn" style="left:512px;top:704px;width:176px;height:40px;line-height:40px">VIEW ALL SERVICES</div>
</section>

<section class="welcome">
  <div class="welcome-photo" role="img" aria-label="Abstract glowing network light bulb above an open hand"></div>
  <h2>WELCOME TO<b>Vorlaufwerkstatt</b></h2>
  <ul>
    <li><svg width="14" height="12" viewBox="0 0 14 12"><path d="M1 6l4 4 8-9" stroke="#e1111d" stroke-width="2.6" fill="none"/></svg>With whom can I implement my innovative idea?</li>
    <li><svg width="14" height="12" viewBox="0 0 14 12"><path d="M1 6l4 4 8-9" stroke="#e1111d" stroke-width="2.6" fill="none"/></svg>Who helps me develop new products, services or business<br>models based on my abilities?</li>
    <li><svg width="14" height="12" viewBox="0 0 14 12"><path d="M1 6l4 4 8-9" stroke="#e1111d" stroke-width="2.6" fill="none"/></svg>How do I become more independent of my existing customers<br>with my own products?</li>
    <li><svg width="14" height="12" viewBox="0 0 14 12"><path d="M1 6l4 4 8-9" stroke="#e1111d" stroke-width="2.6" fill="none"/></svg>Who protects my ideas?</li>
    <li><svg width="14" height="12" viewBox="0 0 14 12"><path d="M1 6l4 4 8-9" stroke="#e1111d" stroke-width="2.6" fill="none"/></svg>Who opens the doors to science for me if I do not know<br>who the right people are?</li>
    <li><svg width="14" height="12" viewBox="0 0 14 12"><path d="M1 6l4 4 8-9" stroke="#e1111d" stroke-width="2.6" fill="none"/></svg>How can I get the latest insights for improving my business<br>processes and who can help me with the implementation in<br>my own company?</li>
    <li><svg width="14" height="12" viewBox="0 0 14 12"><path d="M1 6l4 4 8-9" stroke="#e1111d" stroke-width="2.6" fill="none"/></svg>Who relieves me in carrying out cooperation projects with science?</li>
  </ul>
</section>

<section class="events">
  <h2 class="section-title" style="top:58px">LATEST EVENTS</h2>
  <div class="title-bar" style="top:116px"></div>

  <article class="card" style="left:97px">
    <div class="card-photo" role="img" aria-label="Photo of guests standing at tables during an innovation forum" style="background:linear-gradient(180deg,#c9c4bd,#5a5048)"></div>
    <h3>IoT - what<br>companies want</h3>
    <p>The innovation forum SparkForum initiated at the University of Applied Sciences...</p>
    <div class="btn">READ MORE</div>
  </article>
  <article class="card" style="left:355px">
    <div class="card-photo" role="img" aria-label="Photo of a panel of speakers at a conference" style="background:linear-gradient(180deg,#8b8f96,#2c2e33)"></div>
    <h3>Innovation transfer<br>for the region</h3>
    <p>Nordhafen (fbb). It formed the conclusion of an intensive phase: the conference "spark up"...</p>
    <div class="btn">READ MORE</div>
  </article>
  <article class="card" style="left:612px">
    <div class="card-photo" role="img" aria-label="Group photo of event participants" style="background:linear-gradient(180deg,#9a9da3,#3a3c42)"></div>
    <h3>Our team<br>represented on the...</h3>
    <p>The Student Engineering Office Nordstadt has been a good address for years for the...</p>
    <div class="btn">READ MORE</div>
  </article>
  <article class="card" style="left:870px">
    <div class="card-photo" role="img" aria-label="Illustration of connected industry and cloud systems" style="background:linear-gradient(180deg,#e4ecf3,#9fb6c8)"></div>
    <h3>Embedded engineering<br>discussions IV</h3>
    <p>The Student Engineering Office Nordstadt has been a good address for years for the...</p>
    <div class="btn">READ MORE</div>
  </article>
</section>

<footer class="site-footer">
  <div class="brand"><span class="mark"></span>VORLAUFWERKSTATT</div>

  <div class="f-col" style="left:450px">
    <h4>CONTACT US</h4>
    <div class="f-row"><svg width="10" height="13" viewBox="0 0 10 14"><path d="M5 0a5 5 0 0 0-5 5c0 4 5 9 5 9s5-5 5-9a5 5 0 0 0-5-5z" fill="#fff"/><circle cx="5" cy="5" r="2" fill="#222"/></svg><span>Transferhaus Nord GmbH<br>Lindenweg 8, 30100 Musterfeld</span></div>
    <div class="f-row"><svg width="11" height="11" viewBox="0 0 24 24"><path fill="#fff" d="M6.6 10.8a15 15 0 0 0 6.6 6.6l2.2-2.2c.3-.3.7-.4 1-.2 1.1.4 2.3.6 3.6.6.6 0 1 .4 1 1V20c0 .6-.4 1-1 1A17 17 0 0 1 3 4c0-.6.4-1 1-1h3.5c.6 0 1 .4 1 1 0 1.3.2 2.5.6 3.6z"/></svg><span>+49 5100 24 61 380</span></div>
    <div class="f-row"><svg width="12" height="10" viewBox="0 0 12 10"><rect width="12" height="10" fill="#fff"/><path d="M0 0l6 5 6-5" stroke="#222" fill="none"/></svg><span>info@vorlaufwerkstatt.example</span></div>
  </div>

  <div class="f-col" style="left:750px">
    <h4>MENU</h4>
    <ul class="f-menu" style="margin-top:14px"><li>SERVICES</li><li>REFERENCES</li><li>EVENTS &amp; WORKSHOPS</li><li>REPORTS</li><li>CONTACT</li></ul>
  </div>

  <div class="f-col" style="left:945px">
    <h4>CONNECT WITH US</h4>
    <div class="social"><span class="c"></span>Newsroom</div>
    <div class="social"><span class="c" style="background:#2a9fe6"></span>Microblog</div>
    <div class="social"><span class="c" style="background:#1a3f7a"></span>Career network</div>
  </div>

  <div class="footer-rule"></div>
  <p class="copyright">Copyrights @ 2019 All Rights Reserved</p>
</footer>

</body>
</html>
```